Austin TX First Veterinary Urgent Care

We need a flyer designed for us and our clinic that is eye-catching but also summarizes the advantages of our services. We want to express that we are family owned, have convenient hours and affordable prices. We are the first veterinary urgent care animal clinic in Austin Texas. Our hours of operation are M-F 12PM-9PM S-S 10AM-6PM. Our Address is 8715 W Larkmoor Rd Suite B262 Austin, Tx 78699. Our phone number is (737)555-0148 our website is www.brolliepetco.example and our email address is info@brolliepetco.example.

Target Market(s)

Pet owners and veterinary professionals for referral purposes.

Industry/Entity Type

Veterinary

Font styles to use
Sans Serif

Colors
0094D4
00A9DD
6FCCEA
C7EBF8
E9F6FB
00AB8E
00BBA5
67D7C9
C6EFE9
E9F9F6

Requirements
Must have
• Our logo, hours of operation and contact information easy to read. Should emphasize that we are affordable as well as family owned. List of services should also be displayed: ear, eye, and skin issues, limping, broken toenails, lacerations, coughing, sneezing, allergies, vomiting and diarrhea, urinary issues, constipation, snake bites, toxin ingestion, and many many more
Nice to have
• We would like to have a modern feel with drawn/cartoon images, not realistic stock photos of dogs/cats.

```html
<!DOCTYPE html>
<html lang="en">
<head>
<meta charset="utf-8">
<title>Brollie Pet Co. – Veterinary Urgent Care Flyer</title>
<link rel="stylesheet" href="https://fonts.googleapis.com/css2?family=Poppins:wght@500;600;700;800&display=swap">
<style>
  :root {
    --blue: #0094d4;
    --blue-deep: #00739f;
    --blue-mid: #00a9dd;
    --blue-soft: #6fccea;
    --blue-pale: #c7ebf8;
    --teal: #00ab8e;
    --teal-mid: #00bba5;
    --teal-soft: #67d7c9;
    --teal-pale: #c6efe9;
    --ink: #1e1e1e;
    --paper: #ffffff;
    --backdrop: #d2d2d2;
  }
  * { box-sizing: border-box; margin: 0; padding: 0; }
  html, body { width: 1200px; height: 2324px; overflow: hidden; }
  body { background: var(--backdrop); font-family: "Poppins", sans-serif; color: var(--ink); position: relative; }

  .flyer {
    position: absolute; left: 50px; top: 450px;
    width: 1100px; height: 1424px;
    background: var(--paper);
    box-shadow: 0 6px 18px rgba(0,0,0,.18);
    overflow: hidden;
  }
  .abs { position: absolute; }

  /* brand */
  .brand { left: 66px; top: 72px; display: flex; align-items: center; gap: 16px; }
  .brand-dot { width: 54px; height: 54px; border-radius: 50%; background: var(--teal); }
  .brand-name { font-size: 46px; font-weight: 800; color: var(--blue); line-height: 1; }

  /* headline */
  .headline { left: 66px; line-height: 1; font-weight: 800; white-space: nowrap; }
  .headline.kicker { top: 212px; font-size: 55px; font-weight: 500; color: var(--ink); letter-spacing: 1px; }
  .headline.vet { top: 270px; font-size: 77px; color: var(--teal); }
  .headline.urgent { top: 340px; font-size: 114px; color: var(--blue); }
  .headline.care { top: 440px; font-size: 114px; color: var(--teal); }

  /* illustration areas */
  .art-hero {
    left: 560px; top: 92px; width: 520px; height: 430px;
    border-radius: 55% 45% 20% 20% / 70% 60% 20% 20%;
    background: linear-gradient(180deg, var(--blue) 0%, var(--blue-mid) 50%, var(--blue-soft) 80%, var(--blue-pale) 100%);
  }
  .art-vet {
    left: 50px; top: 672px; width: 443px; height: 440px;
    border-radius: 50% 50% 48% 48% / 48% 48% 40% 40%;
    background: linear-gradient(180deg, var(--blue) 0%, var(--blue-mid) 60%, var(--teal-mid) 85%, var(--teal-soft) 100%);
  }
  .art-pets {
    left: 720px; top: 1066px; width: 250px; height: 107px;
    border-radius: 40px 40px 0 0;
    background: linear-gradient(180deg, var(--teal-pale) 0%, var(--teal-soft) 100%);
  }

  /* benefit band */
  .benefits { left: 69px; top: 545px; width: 964px; height: 96px; border-radius: 22px; overflow: hidden; display: flex; }
  .benefit { display: flex; align-items: center; gap: 16px; padding-left: 24px; color: #fff; font-weight: 700; font-size: 31px; line-height: 1.05; }
  .benefit.family { background: var(--blue); width: 350px; }
  .benefit.value { background: var(--teal); flex: 1; padding-left: 20px; }
  .benefit svg { flex: none; }

  /* services */
  .section-title { font-size: 33px; font-weight: 800; line-height: 1; white-space: nowrap; }
  .section-title .accent { color: var(--blue); }
  .services-title { left: 552px; top: 664px; color: var(--ink); }
  .rule { height: 2px; background: var(--blue); }
  .rule::after { content: ""; position: absolute; right: -3px; top: -3px; width: 8px; height: 8px; border-radius: 50%; background: var(--blue); }
  .services-rule { left: 552px; top: 700px; width: 481px; }
  .services { list-style: none; top: 708px; font-size: 26px; font-weight: 500; line-height: 43px; }
  .services.col-a { left: 552px; }
  .services.col-b { left: 797px; }
  .services li { display: flex; align-items: center; gap: 10px; white-space: nowrap; }
  .tick { width: 15px; height: 15px; flex: none; }

  /* contact */
  .contact-title { left: 66px; top: 1152px; color: var(--blue); font-size: 29px; }
  .contact-title .accent { color: var(--teal); }
  .contact-rule { left: 66px; top: 1192px; width: 545px; }
  .contacts { list-style: none; left: 66px; top: 1212px; font-size: 20px; font-weight: 500; line-height: 38.5px; }
  .contacts li { display: flex; align-items: center; gap: 10px; white-space: nowrap; }
  .contacts svg { width: 24px; height: 24px; flex: none; }

  /* hours */
  .hours { left: 643px; top: 1173px; width: 390px; height: 182px; background: var(--teal); border-radius: 4px; }
  .hours-head { position: absolute; left: 22px; top: 18px; display: flex; align-items: center; gap: 14px; color: #fff; font-weight: 800; font-size: 31px; line-height: 1.05; }
  .hours-table { position: absolute; left: 13px; top: 90px; width: 364px; height: 80px; background: var(--blue-deep); padding: 0 20px; }
  .hours-row { height: 40px; display: flex; align-items: center; gap: 14px; color: #fff; font-weight: 700; font-size: 29px; }
  .hours-row + .hours-row { border-top: 2px solid #fff; }
  .hours-row .time { color: var(--teal-soft); }
</style>
</head>
<body>
<main class="flyer">
  <div class="abs brand">
    <span class="brand-dot"></span>
    <span class="brand-name">Brollie Pet Co.</span>
  </div>

  <h1>
    <span class="abs headline kicker">AUSTIN TX FIRST</span>
    <span class="abs headline vet">VETERINARY</span>
    <span class="abs headline urgent">URGENT</span>
    <span class="abs headline care">CARE</span>
  </h1>

  <div class="abs art-hero" role="img" aria-label="Cartoon dogs sitting in a row in front of a blue paw-print shape"></div>

  <div class="abs benefits">
    <div class="benefit family">
      <svg width="52" height="52" viewBox="0 0 52 52" fill="none" stroke="#fff" stroke-width="2.5" stroke-linejoin="round"><path d="M8 24 26 9l18 15"/><path d="M13 21v20h26V21"/><path d="M26 36s-8-5-8-10a4 4 0 0 1 8-1 4 4 0 0 1 8 1c0 5-8 10-8 10z"/></svg>
      <span>WE ARE<br>FAMILY OWNED</span>
    </div>
    <div class="benefit value">
      <svg width="52" height="52" viewBox="0 0 52 52" fill="none" stroke="#fff" stroke-width="2.5" stroke-linecap="round"><circle cx="24" cy="26" r="17"/><path d="M24 15v11l8 5"/><circle cx="41" cy="40" r="8" fill="var(--teal)"/><path d="M41 35v10M38 37.5h4.5a1.8 1.8 0 0 1 0 3.5h-3a1.8 1.8 0 0 0 0 3.5H44"/></svg>
      <span>HAVE CONVENIENT HOURS AND<br>AFFORDABLE PRICES</span>
    </div>
  </div>

  <div class="abs art-vet" role="img" aria-label="Cartoon veterinarian kneeling with cats and dogs on a grassy patch"></div>

  <h2 class="abs section-title services-title">OUR <span class="accent">SERVICES</span></h2>
  <div class="abs rule services-rule"></div>
  <ul class="abs services col-a">
    <li><svg class="tick" viewBox="0 0 16 16"><circle cx="8" cy="8" r="8" fill="var(--teal)"/><path d="M4.5 8.2 7 10.5l4.5-5" stroke="#fff" stroke-width="2" fill="none"/></svg>Ear</li>
    <li><svg class="tick" viewBox="0 0 16 16"><circle cx="8" cy="8" r="8" fill="var(--teal)"/><path d="M4.5 8.2 7 10.5l4.5-5" stroke="#fff" stroke-width="2" fill="none"/></svg>Eye</li>
    <li><svg class="tick" viewBox="0 0 16 16"><circle cx="8" cy="8" r="8" fill="var(--teal)"/><path d="M4.5 8.2 7 10.5l4.5-5" stroke="#fff" stroke-width="2" fill="none"/></svg>Skin issues</li>
    <li><svg class="tick" viewBox="0 0 16 16"><circle cx="8" cy="8" r="8" fill="var(--teal)"/><path d="M4.5 8.2 7 10.5l4.5-5" stroke="#fff" stroke-width="2" fill="none"/></svg>Limping</li>
    <li><svg class="tick" viewBox="0 0 16 16"><circle cx="8" cy="8" r="8" fill="var(--teal)"/><path d="M4.5 8.2 7 10.5l4.5-5" stroke="#fff" stroke-width="2" fill="none"/></svg>Broken toenails</li>
    <li><svg class="tick" viewBox="0 0 16 16"><circle cx="8" cy="8" r="8" fill="var(--teal)"/><path d="M4.5 8.2 7 10.5l4.5-5" stroke="#fff" stroke-width="2" fill="none"/></svg>Lacerations</li>
    <li><svg class="tick" viewBox="0 0 16 16"><circle cx="8" cy="8" r="8" fill="var(--teal)"/><path d="M4.5 8.2 7 10.5l4.5-5" stroke="#fff" stroke-width="2" fill="none"/></svg>Coughing</li>
    <li><svg class="tick" viewBox="0 0 16 16"><circle cx="8" cy="8" r="8" fill="var(--teal)"/><path d="M4.5 8.2 7 10.5l4.5-5" stroke="#fff" stroke-width="2" fill="none"/></svg>Sneezing</li>
  </ul>
  <ul class="abs services col-b">
    <li><svg class="tick" viewBox="0 0 16 16"><circle cx="8" cy="8" r="8" fill="var(--teal)"/><path d="M4.5 8.2 7 10.5l4.5-5" stroke="#fff" stroke-width="2" fill="none"/></svg>Allergies</li>
    <li><svg class="tick" viewBox="0 0 16 16"><circle cx="8" cy="8" r="8" fill="var(--teal)"/><path d="M4.5 8.2 7 10.5l4.5-5" stroke="#fff" stroke-width="2" fill="none"/></svg>Vomiting and</li>
    <li><svg class="tick" viewBox="0 0 16 16"><circle cx="8" cy="8" r="8" fill="var(--teal)"/><path d="M4.5 8.2 7 10.5l4.5-5" stroke="#fff" stroke-width="2" fill="none"/></svg>Diarrhea</li>
    <li><svg class="tick" viewBox="0 0 16 16"><circle cx="8" cy="8" r="8" fill="var(--teal)"/><path d="M4.5 8.2 7 10.5l4.5-5" stroke="#fff" stroke-width="2" fill="none"/></svg>Urinary</li>
    <li><svg class="tick" viewBox="0 0 16 16"><circle cx="8" cy="8" r="8" fill="var(--teal)"/><path d="M4.5 8.2 7 10.5l4.5-5" stroke="#fff" stroke-width="2" fill="none"/></svg>Issues</li>
    <li><svg class="tick" viewBox="0 0 16 16"><circle cx="8" cy="8" r="8" fill="var(--teal)"/><path d="M4.5 8.2 7 10.5l4.5-5" stroke="#fff" stroke-width="2" fill="none"/></svg>Constipation</li>
    <li><svg class="tick" viewBox="0 0 16 16"><circle cx="8" cy="8" r="8" fill="var(--teal)"/><path d="M4.5 8.2 7 10.5l4.5-5" stroke="#fff" stroke-width="2" fill="none"/></svg>Snake bites</li>
    <li><svg class="tick" viewBox="0 0 16 16"><circle cx="8" cy="8" r="8" fill="var(--teal)"/><path d="M4.5 8.2 7 10.5l4.5-5" stroke="#fff" stroke-width="2" fill="none"/></svg>Toxin ingestion</li>
  </ul>

  <h2 class="abs section-title contact-title">CALL US TO MAKE <span class="accent">AN APPOINTMENT</span></h2>
  <div class="abs rule contact-rule"></div>
  <ul class="abs contacts">
    <li><svg viewBox="0 0 24 24"><circle cx="12" cy="12" r="12" fill="var(--blue)"/><path d="M8 6.5h2.5l1 3-1.5 1a7 7 0 0 0 3.5 3.5l1-1.5 3 1V16a1.5 1.5 0 0 1-1.5 1.5A10 10 0 0 1 6.5 8 1.5 1.5 0 0 1 8 6.5z" fill="var(--teal-pale)"/></svg>(737)555-0148</li>
    <li><svg viewBox="0 0 24 24"><circle cx="12" cy="12" r="12" fill="var(--blue)"/><rect x="6" y="8" width="12" height="8.5" rx="1" fill="var(--teal-pale)"/><path d="M6.5 8.5 12 13l5.5-4.5" stroke="var(--blue)" stroke-width="1.3" fill="none"/></svg>info@brolliepetco.example</li>
    <li><svg viewBox="0 0 24 24"><circle cx="12" cy="12" r="12" fill="var(--blue)"/><circle cx="12" cy="12" r="6.5" fill="none" stroke="var(--teal-pale)" stroke-width="1.5"/><path d="M5.5 12h13M12 5.5c-3 3.5-3 9.5 0 13M12 5.5c3 3.5 3 9.5 0 13" stroke="var(--teal-pale)" stroke-width="1.3" fill="none"/></svg>www.brolliepetco.example</li>
    <li><svg viewBox="0 0 24 24"><circle cx="12" cy="12" r="12" fill="var(--blue)"/><path d="M12 19s-5-5.2-5-9a5 5 0 0 1 10 0c0 3.8-5 9-5 9z" fill="var(--teal-pale)"/><circle cx="12" cy="10" r="1.8" fill="var(--blue)"/></svg>8715 W Larkmoor Rd Suite B262 Austin, Tx 78699</li>
  </ul>

  <div class="abs art-pets" role="img" aria-label="Cartoon cat and puppy peeking over the hours panel"></div>
  <section class="abs hours">
    <div class="hours-head">
      <svg width="44" height="48" viewBox="0 0 44 48" fill="none" stroke="#fff" stroke-width="2.5" stroke-linecap="round"><rect x="3" y="7" width="30" height="32" rx="3"/><path d="M3 16h30M11 3v8M25 3v8"/><circle cx="33" cy="37" r="9" fill="var(--teal)"/><path d="M33 32v5l3 2"/></svg>
      <span>OUR HOURS OF<br>OPERATION ARE</span>
    </div>
    <div class="hours-table">
      <div class="hours-row">
        <svg width="24" height="24" viewBox="0 0 24 24" fill="none" stroke="var(--teal-soft)" stroke-width="2.2" stroke-linecap="round"><circle cx="12" cy="12" r="10"/><path d="M12 6.5V12l4 2"/></svg>
        <span>M-F <span class="time">12PM-9PM</span></span>
      </div>
      <div class="hours-row">
        <svg width="24" height="24" viewBox="0 0 24 24" fill="none" stroke="var(--teal-soft)" stroke-width="2.2" stroke-linecap="round"><circle cx="12" cy="12" r="10"/><path d="M12 6.5V12l4 2"/></svg>
        <span>S-S <span class="time">10AM-6PM</span></span>
      </div>
    </div>
  </section>
</main>
</body>
</html>
```